Car back window and sides sticker for real estate

Dear Designer

We recently developed through PixelForum our new logo (source files attached). Our new website is online since a few days. Now we need a car graphic design for back window and both sides.

The basic design guideline:

- The graphics should be designed for the car sides and back window only. Do not use side windows or hood.

- Refer to the attachment for the actual car and the 4 zones for the design: zone1: front,1m, zone2+3: both doors, 2m, and zone4, back, 1m.

- Back window design max dimension 130cmx75cm.

- We like to see the design in the zones 2 and 3, zone 4 is also possible.

- There are a few must have elements: On the back window there must be our logo with the slogan and on both sides we like to see something like “Follow us on zapline, loopster and vantiq” and our cell phone number. It’s up to you to develop the rest of the design. Social media and hints are very important!

- We prefer discreet design over a too fancy one. No car wrap! Only designs that can be plotted.

- You can pick elements/colors/or ideas from our new website: www.haldenmatt.ch for inspiration.

- Designs need to be simulated on the car picture or another car for reference only.

- Winning designs have to be submitted as vector and in CMYK color mode.

Please fell free to contact us for more information. We will give feedback to all submissions like we deed with our logo development.

UPDATE:

To summit up: Think about like an business card on the back window of a car.

Reason: not the right design yet

Reason: still no new designs, 5 received, far away from what we expect...

• colored social media pictograms zapline, Loopster, vantiq+
cell phone number and our logo

```html
<!DOCTYPE html>
<html lang="de">
<head>
<meta charset="utf-8">
<title>haldenmatt.ch – Fahrzeugbeschriftung</title>
<link rel="stylesheet" href="https://fonts.googleapis.com/css2?family=Lato:wght@400;700&family=Questrial&display=swap">
<style>
  :root {
    --canvas: #ffffff;
    --card-red: #d22027;
    --band-red: #ec1c24;
    --ink: #111111;
    --white: #ffffff;
  }
  html, body {
    margin: 0;
    padding: 0;
    width: 1200px;
    height: 984px;
    overflow: hidden;
    background: var(--canvas);
  }
  .sheet { display: block; width: 1200px; height: 984px; }
  .brand-name { font-family: "Lato", sans-serif; font-weight: 700; fill: var(--white); }
  .slogan { font-family: "Questrial", sans-serif; fill: var(--white); letter-spacing: 1px; }
  .phone-number { font-family: "Lato", sans-serif; font-weight: 700; fill: var(--white); }
  .social-handle { font-family: "Lato", sans-serif; font-weight: 700; fill: var(--white); font-size: 21px; }
  .web-address { font-family: "Lato", sans-serif; font-weight: 700; fill: var(--white); font-size: 42px; }
  .back-window { fill: var(--card-red); }
  .side-band { fill: var(--band-red); }
  .black-strip { fill: var(--ink); }
  .icon-disc { fill: var(--white); }
  .icon-handset { fill: var(--ink); }
  .icon-handset.on-red { fill: var(--card-red); }
  .social-dot { fill: var(--white); }
</style>
</head>
<body>
<svg class="sheet" viewBox="0 0 1200 984" xmlns="http://www.w3.org/2000/svg">
  <defs>
    <linearGradient id="divider-shade" x1="0" x2="1" y1="0" y2="0">
      <stop offset="0" stop-color="#7a0f13" stop-opacity="0"/>
      <stop offset="0.5" stop-color="#7a0f13" stop-opacity="0.8"/>
      <stop offset="1" stop-color="#7a0f13" stop-opacity="0"/>
    </linearGradient>
    <symbol id="handset" viewBox="0 0 24 24">
      <path d="M6.6 10.8c1.4 2.8 3.8 5.1 6.6 6.6l2.2-2.2c.3-.3.7-.4 1-.2 1.1.4 2.3.6 3.6.6.6 0 1 .4 1 1V20c0 .6-.4 1-1 1C10.6 21 3 13.4 3 4c0-.6.4-1 1-1h3.5c.6 0 1 .4 1 1 0 1.3.2 2.5.6 3.6.1.3 0 .7-.2 1l-2.3 2.2z"/>
    </symbol>
  </defs>

  <!-- Back window card -->
  <g class="back-window-card">
    <rect class="back-window" x="202" y="37" width="841" height="419"/>
    <text class="brand-name" x="622" y="185" font-size="70" text-anchor="middle">haldenmatt.ch</text>
    <text class="slogan" x="622" y="228" font-size="34" text-anchor="middle">Wohnen mit Weitblick</text>
    <rect x="240" y="254" width="764" height="4" fill="url(#divider-shade)"/>

    <circle class="icon-disc" cx="462" cy="301" r="20"/>
    <use class="icon-handset on-red" href="#handset" x="450" y="289" width="24" height="24"/>
    <text class="phone-number" x="488" y="318" font-size="50">031 555 18 42</text>

    <circle class="social-dot" cx="258" cy="354" r="6"/>
    <text class="social-handle" x="272" y="361">loopster haldenmatt.ch</text>
    <circle class="social-dot" cx="518" cy="356" r="6"/>
    <text class="social-handle" x="532" y="363">zapline @wohnidee_VS</text>
    <circle class="social-dot" cx="778" cy="354" r="6"/>
    <text class="social-handle" x="792" y="361">vantiq+ haldenmatt.ch</text>

    <polygon class="black-strip" points="412,389 857,389 836,447 391,447"/>
    <text class="web-address" x="624" y="433" text-anchor="middle">www.haldenmatt.ch</text>
  </g>

  <!-- Side band, phone left -->
  <g class="side-band-left">
    <polygon class="side-band" points="184,566 1102,566 1056,729 140,729"/>
    <polygon class="black-strip" points="186,604 615,604 584,693 149,693"/>
    <circle class="icon-disc" cx="209" cy="648" r="22"/>
    <use class="icon-handset" href="#handset" x="195" y="634" width="28" height="28"/>
    <text class="phone-number" x="246" y="667" font-size="50">031 555 18 42</text>
    <text class="brand-name" x="851" y="668" font-size="52" text-anchor="middle">haldenmatt.ch</text>
    <text class="slogan" x="851" y="702" font-size="26" text-anchor="middle">Wohnen mit Weitblick</text>
  </g>

  <!-- Side band, phone right -->
  <g class="side-band-right">
    <polygon class="side-band" points="140,776 1050,776 1098,938 186,938"/>
    <polygon class="black-strip" points="621,811 1050,811 1087,900 652,900"/>
    <circle class="icon-disc" cx="679" cy="856" r="22"/>
    <use class="icon-handset" href="#handset" x="665" y="842" width="28" height="28"/>
    <text class="phone-number" x="716" y="875" font-size="50">031 555 18 42</text>
    <text class="brand-name" x="395" y="875" font-size="52" text-anchor="middle">haldenmatt.ch</text>
    <text class="slogan" x="395" y="909" font-size="26" text-anchor="middle">Wohnen mit Weitblick</text>
  </g>
</svg>
</body>
</html>
```